Single-sided business card for restaurant bellwether with new logo made on this site

Business card options with new logo including restaurant name, address, phone number and website. This business card is single-sided only and will be presented at the hostess desk for clients to take. I would like to see options based on a cream card background, a white card background, a yellow card background and a burgundy colored background. It needs to be elegant and traditional.

Target Market(s)

local and international crowd

Industry/Entity Type

restaurant

Contact Information for Business Card

address, website and phone number

Font styles to use
Serif

Colors
EE7325
F08F49
F5BC92
FAE3D3
FDF4ED

Requirements
Must have
• new logo, address, phone number, website
Should not have
• more than three colors

```html
<!DOCTYPE html>
<html lang="es">
<head>
<meta charset="utf-8">
<title>Bellwether – Business Card Options</title>
<link href="https://fonts.googleapis.com/css2?family=Gelasio:wght@400;500&display=swap" rel="stylesheet">
<style>
  :root {
    --burgundy: #3f1c1d;
    --gold: #f8b42a;
    --cream: #f8f2e1;
    --white: #ffffff;
    --stage-top: #d2d2d2;
    --stage-bottom: #9c9c9c;
    --serif: "Gelasio", Georgia, serif;
  }
  * { margin: 0; padding: 0; box-sizing: border-box; }
  html, body { width: 1200px; height: 795px; overflow: hidden; }
  body {
    position: relative;
    background: linear-gradient(180deg, var(--stage-top), var(--stage-bottom));
    font-family: var(--serif);
  }
  .card {
    position: absolute;
    width: 516px;
    height: 295px;
    border-radius: 27px;
    overflow: hidden;
    box-shadow: 4px 5px 9px rgba(0,0,0,0.35);
    --bg: var(--white);
    --ink: var(--burgundy);
    --accent: var(--gold);
    --rule: var(--gold);
    --band: var(--gold);
    --base: var(--burgundy);
    --mark: var(--burgundy);
    background: var(--bg);
    color: var(--ink);
  }
  .card--burgundy { left: 64px; top: 72px; --bg: var(--burgundy); --ink: var(--white); --accent: var(--gold); --band: var(--white); --base: var(--gold); --mark: var(--white); }
  .card--white { left: 616px; top: 72px; }
  .card--cream { left: 64px; top: 405px; --bg: var(--cream); }
  .card--yellow { left: 616px; top: 405px; --bg: var(--gold); --rule: var(--burgundy); --accent: var(--burgundy); --band: var(--cream); }

  .brand {
    position: absolute;
    left: 92px;
    top: 85px;
    width: 170px;
    text-align: center;
  }
  .brand__square {
    display: block;
    width: 68px;
    height: 68px;
    margin: 0 auto 14px;
    background: var(--mark);
  }
  .brand__name {
    font-size: 19px;
    font-weight: 500;
    letter-spacing: 2.5px;
    color: var(--mark);
    line-height: 1;
  }
  .divider {
    position: absolute;
    left: 257px;
    top: 86px;
    width: 1.5px;
    height: 124px;
    background: var(--rule);
  }
  .details {
    position: absolute;
    left: 278px;
    top: 92px;
    font-size: 13.5px;
    letter-spacing: 0.4px;
    line-height: 19px;
  }
  .details__address { margin-bottom: 16px; }
  .details__list { list-style: none; }
  .details__list li { display: flex; align-items: center; gap: 5px; height: 19px; }
  .icon { width: 12px; height: 12px; flex: none; }
  .icon__disc { fill: var(--accent); }
  .icon__glyph { fill: var(--bg); stroke: var(--bg); }
  .wave { position: absolute; left: 0; top: 0; width: 516px; height: 295px; }
  .wave__band { fill: var(--band); }
  .wave__base { fill: var(--base); }
</style>
</head>
<body>
<svg width="0" height="0" style="position:absolute" aria-hidden="true">
  <defs>
    <symbol id="icon-phone" viewBox="0 0 12 12">
      <circle class="icon__disc" cx="6" cy="6" r="6"/>
      <path class="icon__glyph" stroke="none" d="M3.6 2.8c.4-.3.8-.2 1 .2l.5 1c.2.4 0 .7-.3.9l-.3.2c.3.8.9 1.5 1.7 1.9l.3-.3c.3-.3.6-.4 1-.2l1 .5c.4.2.4.7.1 1l-.5.5c-.6.5-1.6.3-2.7-.5S3.4 6 3 4.9c-.3-.9 0-1.6.6-2.1z"/>
    </symbol>
    <symbol id="icon-mail" viewBox="0 0 12 12">
      <circle class="icon__disc" cx="6" cy="6" r="6"/>
      <rect class="icon__glyph" stroke="none" x="2.8" y="3.8" width="6.4" height="4.4" rx="0.5"/>
      <path d="M3 4.1 6 6.4 9 4.1M3 8 5 6M9 8 7 6" fill="none" style="stroke:var(--accent)" stroke-width="0.7"/>
    </symbol>
    <symbol id="icon-web" viewBox="0 0 12 12">
      <circle class="icon__disc" cx="6" cy="6" r="6"/>
      <circle cx="6" cy="6" r="3.3" fill="none" class="icon__glyph" style="fill:none" stroke-width="0.8"/>
      <path d="M2.7 6h6.6M6 2.7c-1.4 1.8-1.4 4.8 0 6.6M6 2.7c1.4 1.8 1.4 4.8 0 6.6" fill="none" class="icon__glyph" style="fill:none" stroke-width="0.7"/>
    </symbol>
  </defs>
</svg>

<article class="card card--burgundy">
  <svg class="wave" viewBox="0 0 516 295" aria-hidden="true">
    <path class="wave__band" d="M0 246 C90 274 200 273 330 250 C420 234 478 233 516 252 L516 261 C478 243 420 242 330 258 C200 281 90 283 0 251 Z"/>
    <path class="wave__base" d="M0 253 C90 286 200 283 330 262 C420 248 480 246 516 268 L516 295 L0 295 Z"/>
  </svg>
  <div class="brand"><span class="brand__square"></span><p class="brand__name">BELLWETHER</p></div>
  <span class="divider"></span>
  <div class="details">
    <p class="details__address">Jazmín 418 Bahías De<br>Santa Cruz, Oaxaca Cp 70950</p>
    <ul class="details__list">
      <li><svg class="icon"><use href="#icon-phone"/></svg>958-555-0142</li>
      <li><svg class="icon"><use href="#icon-mail"/></svg>info@bellwether.com.mx</li>
      <li><svg class="icon"><use href="#icon-web"/></svg>www.bellwether.com.mx</li>
    </ul>
  </div>
</article>

<article class="card card--white">
  <svg class="wave" viewBox="0 0 516 295" aria-hidden="true">
    <path class="wave__band" d="M0 246 C90 274 200 273 330 250 C420 234 478 233 516 252 L516 268 C478 246 420 248 330 262 C200 283 90 286 0 253 Z"/>
    <path class="wave__base" d="M0 253 C90 288 200 284 330 264 C420 250 480 248 516 270 L516 295 L0 295 Z"/>
  </svg>
  <div class="brand"><span class="brand__square"></span><p class="brand__name">BELLWETHER</p></div>
  <span class="divider"></span>
  <div class="details">
    <p class="details__address">Jazmín 418 Bahías De<br>Santa Cruz, Oaxaca Cp 70950</p>
    <ul class="details__list">
      <li><svg class="icon"><use href="#icon-phone"/></svg>958-555-0142</li>
      <li><svg class="icon"><use href="#icon-mail"/></svg>info@bellwether.com.mx</li>
      <li><svg class="icon"><use href="#icon-web"/></svg>www.bellwether.com.mx</li>
    </ul>
  </div>
</article>

<article class="card card--cream">
  <svg class="wave" viewBox="0 0 516 295" aria-hidden="true">
    <path class="wave__band" d="M0 246 C90 274 200 273 330 250 C420 234 478 233 516 252 L516 268 C478 246 420 248 330 262 C200 283 90 286 0 253 Z"/>
    <path class="wave__base" d="M0 253 C90 288 200 284 330 264 C420 250 480 248 516 270 L516 295 L0 295 Z"/>
  </svg>
  <div class="brand"><span class="brand__square"></span><p class="brand__name">BELLWETHER</p></div>
  <span class="divider"></span>
  <div class="details">
    <p class="details__address">Jazmín 418 Bahías De<br>Santa Cruz, Oaxaca Cp 70950</p>
    <ul class="details__list">
      <li><svg class="icon"><use href="#icon-phone"/></svg>958-555-0142</li>
      <li><svg class="icon"><use href="#icon-mail"/></svg>info@bellwether.com.mx</li>
      <li><svg class="icon"><use href="#icon-web"/></svg>www.bellwether.com.mx</li>
    </ul>
  </div>
</article>

<article class="card card--yellow">
  <svg class="wave" viewBox="0 0 516 295" aria-hidden="true">
    <path class="wave__band" d="M0 246 C90 274 200 273 330 250 C420 234 478 233 516 252 L516 268 C478 246 420 248 330 262 C200 283 90 286 0 253 Z"/>
    <path class="wave__base" d="M0 253 C90 288 200 284 330 264 C420 250 480 248 516 270 L516 295 L0 295 Z"/>
  </svg>
  <div class="brand"><span class="brand__square"></span><p class="brand__name">BELLWETHER</p></div>
  <span class="divider"></span>
  <div class="details">
    <p class="details__address">Jazmín 418 Bahías De<br>Santa Cruz, Oaxaca Cp 70950</p>
    <ul class="details__list">
      <li><svg class="icon"><use href="#icon-phone"/></svg>958-555-0142</li>
      <li><svg class="icon"><use href="#icon-mail"/></svg>info@bellwether.com.mx</li>
      <li><svg class="icon"><use href="#icon-web"/></svg>www.bellwether.com.mx</li>
    </ul>
  </div>
</article>
</body>
</html>
```